Visual Print Advert for Hair & Makeup Artist

One page colour visual advertisement required for a hair and makeup artist business using pictures and logo with brief description and contact details. MUST have plain white background. All information will be provided I just need someone to put it in a good layout.
Professional, clean and appealing to the eye. Don't want it to look over crowded or busy.
Layout should feature 2-7 photos, without making the page look too busy. Can use any of the photos provided and you are welcome to crop them to change the orientation of the photo.
Content and typeface should fit in with logo and be modern but appeal to the female target audience of brides in Australia aged 22-40yo.
Advertisement is be be used in a bridal magazine and other print media for business advertising purposes.
Updates

Ad is to be A4 size, portrait orientation Added Monday, December 26, 2016

Target Market(s)

Future brides in Australia aged 22 - 40yo - females only

Industry/Entity Type

Business

Colors
e34197
ffffff
eda3c7

Requirements
Must have
• White background
Should not have
• NO script writing as it doesn't fit with the logo.

```html
<!DOCTYPE html>
<html lang="en">
<head>
<meta charset="utf-8">
<title>Avelle Makeup Artistry – Bridal Advert</title>
<link href="https://fonts.googleapis.com/css2?family=Josefin+Sans:wght@300;400&display=swap" rel="stylesheet">
<style>
  :root{
    --pink-deep:#e34197;
    --pink-soft:#f59ad8;
    --pink-pale:#eda3c7;
    --white:#ffffff;
    --ink:#2b2b2b;
    --grey-band:#ebebeb;
    --grey-light:#f5f5f5;
    --grey-dark:#4a4a4a;
  }
  html,body{margin:0;padding:0;overflow:hidden;background:var(--white);}
  .advert{
    position:relative;width:1041px;height:1200px;overflow:hidden;
    background:var(--white);
    font-family:"Josefin Sans",sans-serif;color:var(--ink);
  }
  .advert__shapes{position:absolute;inset:0;}
  .brand{position:absolute;left:82px;top:44px;width:463px;text-align:right;}
  .brand__name{
    display:block;text-align:left;font-weight:300;font-size:72px;
    letter-spacing:14px;line-height:1;color:var(--ink);
  }
  .brand__tagline{
    display:block;margin-top:10px;font-weight:400;font-size:15px;
    letter-spacing:4px;color:var(--grey-dark);
  }
  .intro{
    position:absolute;left:82px;top:290px;margin:0;
    font-weight:300;font-size:27px;line-height:31px;letter-spacing:0.4px;
    white-space:nowrap;
  }
  .credentials{
    position:absolute;left:82px;top:536px;margin:0;
    font-weight:300;font-size:38px;line-height:44.5px;letter-spacing:0.4px;
    white-space:nowrap;
  }
  .accent{color:var(--pink-deep);}
  .contact{
    position:absolute;left:537px;top:1072px;margin:0;padding:0;list-style:none;
    font-weight:300;font-size:26px;letter-spacing:0.6px;color:var(--ink);
  }
  .contact__item{display:flex;align-items:center;height:35px;}
  .contact__icon{width:22px;height:22px;margin-right:20px;flex:none;}
</style>
</head>
<body>
<div class="advert">
  <svg class="advert__shapes" width="1041" height="1200" viewBox="0 0 1041 1200">
    <defs>
      <linearGradient id="bridePortraitTone" x1="0" y1="0" x2="1" y2="1">
        <stop offset="0" stop-color="#9a9593"/>
        <stop offset="0.4" stop-color="#c59a84"/>
        <stop offset="0.72" stop-color="#e6e2df"/>
        <stop offset="1" stop-color="#5a2a28"/>
      </linearGradient>
      <linearGradient id="gardenTone" x1="0" y1="0" x2="1" y2="1">
        <stop offset="0" stop-color="#9fb07a"/>
        <stop offset="1" stop-color="#d9c7b8"/>
      </linearGradient>
      <linearGradient id="hairTone" x1="0" y1="0" x2="1" y2="1">
        <stop offset="0" stop-color="#f1ece8"/>
        <stop offset="1" stop-color="#9a5a3a"/>
      </linearGradient>
      <linearGradient id="carTone" x1="0" y1="0" x2="1" y2="1">
        <stop offset="0" stop-color="#8f9a6a"/>
        <stop offset="1" stop-color="#b5362f"/>
      </linearGradient>
      <linearGradient id="columnTone" x1="0" y1="0" x2="0" y2="1">
        <stop offset="0" stop-color="#f4f4f4"/>
        <stop offset="1" stop-color="#ffffff"/>
      </linearGradient>
    </defs>

    <!-- soft grey header arc, tapered at both ends -->
    <path class="header-arc" d="M0 168 C110 232 300 246 540 188 C320 224 120 212 0 140 Z" fill="var(--grey-band)"/>

    <!-- main portrait area -->
    <path role="img" aria-label="Photograph: bride in a strapless beaded gown with veil, looking down"
      d="M1041 1015 L560 1015 C440 880 385 600 470 350 C510 250 570 185 650 150 C770 105 900 95 1041 112 Z"
      fill="url(#bridePortraitTone)"/>

    <!-- pink swoosh at the top -->
    <path class="header-swoosh" d="M378 196 C560 172 700 92 840 76 C940 66 1000 80 1041 100 L1041 171 C990 140 920 116 830 119 C680 126 560 180 378 196 Z" fill="var(--pink-soft)"/>

    <!-- bottom band and pink waves -->
    <path class="footer-band" d="M300 1060 C520 1040 700 1005 1041 962 L1041 1200 L300 1200 Z" fill="var(--grey-light)"/>
    <path class="footer-dark" d="M880 1002 C940 990 990 975 1041 962 L1041 1040 C990 1012 940 1002 880 1002 Z" fill="var(--grey-dark)"/>
    <path class="footer-wave" d="M0 1032 C60 1030 120 1058 200 1070 L200 1092 C120 1092 60 1098 0 1102 Z" fill="var(--pink-soft)"/>
    <path class="footer-wave" d="M460 1032 C560 1020 640 1002 700 992 C640 1010 560 1032 460 1046 Z" fill="var(--pink-soft)"/>

    <!-- gallery circles -->
    <circle cx="172" cy="1049" r="108" fill="var(--pink-soft)"/>
    <circle role="img" aria-label="Photograph: bride with an updo in a garden" cx="172" cy="1049" r="99" fill="url(#gardenTone)"/>
    <circle cx="370" cy="1016" r="106" fill="var(--pink-soft)"/>
    <circle role="img" aria-label="Photograph: braided bridal hairstyle with pink flowers" cx="370" cy="1016" r="97" fill="url(#hairTone)"/>
    <circle cx="862" cy="980" r="106" fill="var(--pink-soft)"/>
    <circle role="img" aria-label="Photograph: smiling bride leaning on a vintage car" cx="862" cy="980" r="97" fill="url(#carTone)"/>

    <!-- social network placeholders -->
    <circle cx="338" cy="1159" r="16" fill="var(--pink-soft)"/>
    <circle cx="385" cy="1159" r="16" fill="var(--pink-soft)"/>
    <circle cx="432" cy="1159" r="16" fill="var(--pink-soft)"/>
    <circle cx="479" cy="1159" r="16" fill="var(--pink-soft)"/>
  </svg>

  <div class="brand">
    <span class="brand__name">AVELLE</span>
    <span class="brand__tagline">MAKEUP ARTISTRY</span>
  </div>

  <p class="intro">We Specialize in<br>naturally enhancing<br>your beauty to<br>have you looking and<br>feeling your best on<br>your <span class="accent">special day.</span></p>

  <p class="credentials">Professionally<br>trained and<br>certified<br>mobile Hair &amp;<br>Makeup Artists<br>with over<br><span class="accent">10 years<br>Experience</span></p>

  <ul class="contact">
    <li class="contact__item">
      <svg class="contact__icon" viewBox="0 0 24 24" fill="none" stroke="var(--pink-soft)" stroke-width="1.6"><circle cx="12" cy="12" r="10.5"/><path d="M8.5 7 l2 2.2 -1 1.3 c.8 1.6 1.8 2.6 3.2 3.3 l1.3-1 2.2 2 -1.2 1.7 c-3.6-.4-6.8-3.6-7.2-7.2 Z" fill="var(--pink-soft)" stroke="none"/></svg>
      0400 123 456
    </li>
    <li class="contact__item">
      <svg class="contact__icon" viewBox="0 0 24 24" fill="none" stroke="var(--pink-soft)" stroke-width="1.6"><rect x="3" y="6" width="18" height="12"/><path d="M3 6 L12 13 L21 6"/></svg>
      mia@avellemakeup.com.au
    </li>
    <li class="contact__item">
      <svg class="contact__icon" viewBox="0 0 24 24" fill="none" stroke="var(--pink-soft)" stroke-width="1.6"><circle cx="12" cy="12" r="9.5"/><ellipse cx="12" cy="12" rx="4" ry="9.5"/><path d="M2.5 12 H21.5 M4 7 H20 M4 17 H20"/></svg>
      www.avellemakeup.com.au
    </li>
  </ul>
</div>
</body>
</html>
```